Label for Dog Nourishing CBD Balm

Dear Designers,

We are looking for a packaging expert to design our new Hydrating Balm for dogs which contain a relaxing hemp extract (CBD). The product is intended to be massaged on the dog’s paws to make them softer and promote the animal’s well-being :)

Our company is already selling various relaxing cat & dog products, and we would like this new design to reflect the same "style & feeling" as our current products (see attached ZIP file).

Technical aspects:
- The packaging is a 40ml aluminium jar (58mm x 23mm).
- We are looking to design 2 separate labels (one for the front, one for the back)
- The label dimensions should be : 50mm x 50mm
- Please follow technical guidelines from printer (see ZIP file).

Design aspects:
- The design should be compatible with our brand identity (i.e. fluffly, pure, relaxing, positive, clean & natural).
- People should understand what the product "is" and what the product "does" simply from looking at the design.
- The actual balm is white/yellow in color.
- Soft/rounded shapes are preferred.
- Please use our brand's colors (see typo & colors in ZIP file)
- Please use our brand's fonts (see typo & colors in ZIP file)
- Please use our company logo (see ZIP file).
- The design also needs to convey a strong sense of professionalism as we are an animal "healthcare" brand.
- If you want to include a dog picture, we would prefer you to use a picture of our official brand ambassador (see ZIP file).
- Only original work (no plagiarism will be accepted).

Please don't hesitate to send us a message if you have any questions about the brand, the product or the design requirements.

We look forward to seeing your designs & working on this together !

Thanks & regards,
Marcus

Target Market(s)

Dog owners

Font styles to use
Other font styles liked:
• See ZIP file

Requirements
Must have
• Brand fonts (see typo & colors in ZIP file)
Brand colors (see typo & colors in ZIP file)

```html
<!DOCTYPE html>
<html lang="en">
<head>
<meta charset="utf-8">
<title>Verabalm Soothing Balm – Front Label</title>
<link rel="stylesheet" href="https://fonts.googleapis.com/css2?family=Bitter:wght@500;600&family=Questrial&display=swap">
<style>
  :root {
    --page: #ffffff;
    --label: #ededed;
    --rim: #d6d6d6;
    --green: #35977a;
    --ink: #1f2a22;
    --paw: #a9cbb9;
    --white: #ffffff;
  }
  html, body {
    margin: 0;
    padding: 0;
    width: 1200px;
    height: 1200px;
    overflow: hidden;
    background: var(--page);
  }
  .label {
    display: block;
    width: 1200px;
    height: 1200px;
  }
  .label__face { fill: var(--label); stroke: var(--rim); stroke-width: 4; }
  .label__crest { fill: none; stroke: var(--green); stroke-linecap: round; stroke-linejoin: round; }
  .label__lower { fill: var(--green); }
  .brand-dot { fill: var(--green); }
  .brand-name {
    font-family: "Bitter", Georgia, serif;
    font-weight: 600;
    font-size: 64px;
    fill: var(--ink);
    letter-spacing: 1px;
  }
  .brand-tagline {
    font-family: "Bitter", Georgia, serif;
    font-weight: 500;
    font-size: 24px;
    fill: var(--green);
  }
  .product-name {
    font-family: "Questrial", "Helvetica Neue", sans-serif;
    font-size: 94px;
    fill: var(--green);
    letter-spacing: 2px;
  }
  .product-type {
    font-family: "Questrial", "Helvetica Neue", sans-serif;
    font-size: 38px;
    fill: var(--ink);
    letter-spacing: 1px;
  }
  .benefits-box { fill: none; stroke: var(--white); stroke-width: 3; }
  .benefits {
    font-family: "Questrial", "Helvetica Neue", sans-serif;
    font-size: 31px;
    fill: var(--white);
    letter-spacing: 1px;
  }
  .spec {
    font-family: "Questrial", "Helvetica Neue", sans-serif;
    font-size: 30px;
    fill: var(--white);
  }
  .spec-rule { stroke: var(--white); stroke-width: 2.5; }
  .weight {
    font-family: "Questrial", "Helvetica Neue", sans-serif;
    font-size: 36px;
    fill: var(--white);
  }
  .paw-trail { opacity: 0.35; }
</style>
</head>
<body>
<svg class="label" viewBox="0 0 1200 1200" xmlns="http://www.w3.org/2000/svg">
  <defs>
    <clipPath id="label-shape">
      <circle cx="600" cy="600" r="480"/>
    </clipPath>
    <linearGradient id="paw-fade" x1="0" y1="0" x2="0" y2="1">
      <stop offset="0" stop-color="#a9cbb9" stop-opacity="1"/>
      <stop offset="1" stop-color="#a9cbb9" stop-opacity="0.5"/>
    </linearGradient>
  </defs>

  <circle class="label__face" cx="600" cy="600" r="480"/>

  <g clip-path="url(#label-shape)">
    <rect class="label__lower" x="100" y="625" width="1000" height="480"/>

    <path class="label__crest" stroke-width="12" d="M 180 196 L 540 196"/>
    <path class="label__crest" stroke-width="12" d="M 660 196 L 1020 196"/>
    <path class="label__crest" stroke-width="6" d="M 540 196 Q 592 200 600 252 Q 608 200 660 196"/>

    <rect class="paw-trail" x="210" y="300" width="95" height="285" rx="47" fill="url(#paw-fade)"
          role="img" aria-label="Scattered paw print decoration"/>
    <rect class="paw-trail" x="895" y="300" width="95" height="285" rx="47" fill="url(#paw-fade)"
          role="img" aria-label="Scattered paw print decoration"/>
  </g>

  <g class="brand">
    <circle class="brand-dot" cx="600" cy="300" r="22"/>
    <text class="brand-name" x="600" y="404" text-anchor="middle">VERDALIA</text>
    <text class="brand-tagline" x="775" y="442" text-anchor="end">For Animals</text>
  </g>

  <text class="product-name" x="600" y="530" text-anchor="middle">VERABALM</text>
  <text class="product-type" x="600" y="588" text-anchor="middle">SOOTHING BALM</text>

  <rect class="benefits-box" x="318" y="633" width="564" height="52" rx="6"/>
  <text class="benefits" x="600" y="670" text-anchor="middle">REPAIR • NOURISH • PROTECT</text>

  <text class="spec" x="640" y="742" text-anchor="end">CBD 250MG</text>
  <line class="spec-rule" x1="655" y1="712" x2="655" y2="754"/>
  <text class="spec" x="670" y="742" text-anchor="start">0% THC</text>
  <line class="spec-rule" x1="440" y1="766" x2="830" y2="766"/>

  <text class="weight" x="600" y="830" text-anchor="middle">40g</text>
</svg>
</body>
</html>
```